2021 Course Calendar

Need to create an instagram sized calendar for 2021

Black background please

Vigour Meridian /10 CEC logos at bottom

Stridewell Coaching Institute logo at top corner

Need to Include the following

COURSES 2021
JAN - Perth / Melbourne
FEB - Brisbane / Sydney
MAR - Perth / Adelaide
APR - Brisbane / Sydney
MAY - Perth / Melbourne
JUN - Adelaide / Brisbane

visit www.stridewellcoachinginstitute.com.au for more info

```html
<!DOCTYPE html>
<html lang="en">
<head>
<meta charset="utf-8">
<title>Courses 2021 – Stridewell Coaching Institute</title>
<link rel="stylesheet" href="https://fonts.googleapis.com/css2?family=Montserrat:wght@500;600;800;900&display=swap">
<style>
  :root {
    --ink: #ffffff;
    --rule: #ffffff;
    --bg-deep: #0d0d0e;
    --bg-mid: #2b2927;
    --bg-warm: #3a332d;
    --badge: #3ed1d9;
  }
  * { box-sizing: border-box; margin: 0; padding: 0; }
  html, body { width: 1200px; height: 1200px; overflow: hidden; background: var(--bg-deep); }
  .poster {
    position: relative;
    width: 1200px;
    height: 1200px;
    overflow: hidden;
    color: var(--ink);
    font-family: "Montserrat", Arial, sans-serif;
  }
  .poster__photo {
    position: absolute;
    inset: 0;
    background:
      radial-gradient(ellipse 40% 55% at 30% 40%, rgba(90,80,70,.55), transparent 70%),
      radial-gradient(ellipse 35% 50% at 85% 45%, rgba(70,90,95,.45), transparent 70%),
      linear-gradient(160deg, var(--bg-warm) 0%, var(--bg-mid) 45%, var(--bg-deep) 100%);
  }
  .brand {
    position: absolute;
    left: 11px;
    top: 8px;
    font-weight: 600;
    font-size: 31px;
    line-height: 39px;
    letter-spacing: .5px;
    text-transform: uppercase;
  }
  .title {
    position: absolute;
    left: 0;
    right: 0;
    top: 112px;
    text-align: center;
    font-weight: 900;
    font-size: 60px;
    letter-spacing: 3px;
    line-height: 1;
  }
  .calendar {
    position: absolute;
    left: 113px;
    top: 223px;
    width: 974px;
    height: 660px;
  }
  .calendar__rule {
    position: absolute;
    left: 0;
    width: 974px;
    height: 8px;
    background: var(--rule);
  }
  .calendar__divider {
    position: absolute;
    left: 480px;
    top: 0;
    width: 7px;
    height: 660px;
    background: var(--rule);
  }
  .month {
    position: absolute;
    width: 484px;
    height: 212px;
  }
  .month__name {
    position: absolute;
    left: 3px;
    top: 24px;
    font-weight: 900;
    font-size: 37px;
    letter-spacing: 1px;
    line-height: 1;
  }
  .month__cities {
    position: absolute;
    left: 10px;
    right: 0;
    top: 118px;
    text-align: center;
    font-weight: 800;
    font-size: 26px;
    letter-spacing: 1.5px;
    line-height: 1;
    white-space: nowrap;
  }
  .month--right .month__name { left: 2px; }
  .website {
    position: absolute;
    left: 0;
    right: 0;
    top: 930px;
    text-align: center;
    font-weight: 600;
    font-size: 26px;
    letter-spacing: .5px;
    line-height: 1;
  }
  .website strong { font-weight: 800; }
  .partner {
    position: absolute;
    left: 0;
    bottom: 8px;
    height: 68px;
    display: flex;
    align-items: center;
    gap: 14px;
    padding: 0 28px 0 18px;
    background: rgba(13,13,14,.6);
  }
  .partner__mark {
    width: 30px;
    height: 30px;
    background: var(--badge);
  }
  .partner__name {
    font-weight: 800;
    font-size: 28px;
    letter-spacing: .5px;
    color: var(--ink);
  }
</style>
</head>
<body>
<main class="poster">
  <div class="poster__photo" role="img" aria-label="Dim gym photograph of two people sitting on a bench wrapping boxing hand wraps"></div>

  <div class="brand">Stridewell<br>Coaching<br>Institute</div>

  <h1 class="title">COURSES 2021</h1>

  <section class="calendar" aria-label="2021 course dates">
    <div class="calendar__rule" style="top:0"></div>
    <div class="calendar__rule" style="top:220px"></div>
    <div class="calendar__rule" style="top:440px"></div>
    <div class="calendar__divider"></div>

    <div class="month" style="left:0;top:8px"><span class="month__name">JAN</span><span class="month__cities">PERTH / MELBOURNE</span></div>
    <div class="month" style="left:0;top:228px"><span class="month__name">FEB</span><span class="month__cities">BRISBANE / SYDNEY</span></div>
    <div class="month" style="left:0;top:448px"><span class="month__name">MAR</span><span class="month__cities">PERTH / ADELAIDE</span></div>

    <div class="month month--right" style="left:487px;top:8px"><span class="month__name">APR</span><span class="month__cities">BRISBANE / SYDNEY</span></div>
    <div class="month month--right" style="left:487px;top:228px"><span class="month__name">MAY</span><span class="month__cities">PERTH / MELBOURNE</span></div>
    <div class="month month--right" style="left:487px;top:448px"><span class="month__name">JUN</span><span class="month__cities">ADELAIDE / BRISBANE</span></div>
  </section>

  <p class="website">visit <strong>www.stridewellcoachinginstitute.com.au</strong> for more info</p>

  <div class="partner">
    <span class="partner__mark"></span>
    <span class="partner__name">Vigour Meridian 10 CECs</span>
  </div>
</main>
</body>
</html>
```